Northern Terrain Published Photographer Website

I need a website to feature a home page slide show of 6 of my top photos then a few simple pages including; gallery, bio, social, checkout, services
Updates

Need extra days to review

Target Market(s)

photography

Industry/Entity Type

Photographer

Coding

Coded - Design and coding required

Number of Pages Required

5+ page

Colors

Designer to choose colors to be used in the design.

Requirements
Must have
• clean eye catching elegant trendy
Nice to have
• unique and creative from other photographer websites

```html
<!DOCTYPE html>
<html lang="en">
<head>
<meta charset="utf-8">
<title>Northern Terrain Photography</title>
<link href="https://fonts.googleapis.com/css2?family=Playfair+Display:wght@400;700;900&family=Oswald:wght@400;500&family=Libre+Baskerville&display=swap" rel="stylesheet">
<style>
:root{
  --ink:#111111;
  --white:#ffffff;
  --panel:#e6e6e6;
  --text:#444444;
  --muted:#888888;
}
*{margin:0;padding:0;box-sizing:border-box}
html,body{width:1200px;height:3564px;overflow:hidden;background:var(--white)}
body{position:relative;font-family:"Libre Baskerville",Georgia,serif;color:var(--ink)}
.abs{position:absolute}
.display{font-family:"Playfair Display",Georgia,serif;font-weight:700}
.label{font-family:"Oswald","Arial Narrow",sans-serif;text-transform:uppercase;letter-spacing:1.5px}

/* header */
.hero-block{left:0;top:0;width:556px;height:798px;background:var(--ink)}
.brand{display:flex;align-items:center;gap:14px;color:var(--white);font-family:"Playfair Display",Georgia,serif;font-weight:400;font-size:30px;white-space:nowrap}
.brand-dot{width:26px;height:26px;border:2px solid var(--white);border-radius:50%}
.nav{left:687px;top:90px;display:flex;gap:30px;font-size:13px;color:var(--ink)}
.icon{width:28px;height:28px;border-radius:50%;border:2px solid var(--ink);display:flex;align-items:center;justify-content:center}
.icon.solid{background:var(--ink)}
.hero-photo{left:88px;top:200px;width:511px;height:510px;background:linear-gradient(160deg,#3c4c60 0%,#2b3a4c 45%,#d8c7cf 70%,#e9e6e6 100%)}
.welcome{left:687px;top:330px;font-size:57px}
.copy{font-size:13px;line-height:21px;color:var(--text)}
.btn{background:var(--ink);color:var(--white);font-size:12px;display:flex;align-items:center;justify-content:center}

.services-title{left:0;width:1200px;top:920px;text-align:center;font-size:38px;line-height:50px}

/* gallery */
.gallery-panel{left:644px;top:1160px;width:556px;height:710px;background:var(--panel)}
.counter{left:900px;top:1240px;width:100px;text-align:center;font-size:11px;color:var(--muted)}
.card{box-shadow:0 18px 40px rgba(0,0,0,.18)}
.stem{width:2px;background:var(--ink)}
.cat{font-size:24px;text-align:center;width:200px}
.cat span{border-bottom:2px solid var(--ink);padding-bottom:4px}
.arrow{width:28px;height:28px;border-radius:50%;background:#e3e3e3;display:flex;align-items:center;justify-content:center}

/* about */
.about-title{left:250px;top:1998px;width:199px;text-align:right;font-size:40px;line-height:48px}

/* subscribe */
.subscribe-bg{left:0;top:2229px;width:1200px;height:392px;background:linear-gradient(90deg,#3b3a2a 0%,#4c5a2e 30%,#5b4a36 60%,#7a6452 80%,#4a3b30 100%)}
.subscribe-box{left:280px;top:2329px;width:640px;height:190px;background:var(--panel);text-align:center}
.subscribe-box h2{font-size:38px;margin-top:28px}
.subscribe-box p{font-size:12px;color:var(--text);margin-top:6px}
.signup{position:absolute;left:179px;top:118px;display:flex}
.signup .field{width:201px;height:34px;background:var(--white);font-size:10px;color:var(--muted);display:flex;align-items:center;padding-left:14px}
.signup .btn{width:81px;height:34px}

/* instagram */
.insta-word{font-family:"Playfair Display",Georgia,serif;font-weight:900;font-size:86px;line-height:1}
.tile{width:233px;height:233px}

/* footer */
.footer{left:0;top:3172px;width:1200px;height:392px;background:var(--ink)}
.foot-link{color:var(--white);font-size:13px}
.legal{color:var(--white);font-size:11px}
.icon.light{border-color:var(--white)}
</style>
</head>
<body>

<header>
  <div class="abs hero-block"></div>
  <div class="abs brand" style="left:88px;top:72px">Northern Terrain<span class="brand-dot"></span></div>
  <nav class="abs nav label">
    <span>My Story</span><span>Services</span><span>Gallery</span><span>Contact</span>
  </nav>
  <div class="abs icon" style="left:1048px;top:86px"></div>
  <div class="abs icon" style="left:1086px;top:86px"></div>
  <div class="abs icon solid" style="left:1124px;top:86px">
    <svg width="14" height="14" viewBox="0 0 14 14"><path d="M1 2h2l2 7h6l2-5H4" fill="none" stroke="#fff" stroke-width="1.6"/><circle cx="6" cy="12" r="1.2" fill="#fff"/><circle cx="10" cy="12" r="1.2" fill="#fff"/></svg>
  </div>
</header>

<section class="hero">
  <div class="abs hero-photo card" role="img" aria-label="Photographer seated on the bow of a boat on open water"></div>
  <h1 class="abs display welcome">Welcome</h1>
  <p class="abs copy" style="left:687px;top:405px;width:410px">Lorem ipsum dolor sit amet, consectetur adipiscing elit. Aenean mattis mi quis tellus convallis, sit amet aliquet massa ornare. Orci varius natoque penatibus et magni. Lorem dolor sit amet, consectetur adipiscing elit.</p>
  <div class="abs btn label" style="left:687px;top:535px;width:121px;height:38px">Learn More</div>
</section>

<section class="services">
  <h2 class="abs display services-title">Service Lorem ipsum dolor amet,<br>consectetur adipiscing elit.</h2>

  <div class="abs gallery-panel"></div>
  <div class="abs counter">- 3/5 -</div>

  <div class="abs card" style="left:88px;top:1247px;width:321px;height:321px;background:linear-gradient(160deg,#e8edf0 0%,#b9a45a 40%,#6d7a2e 70%,#3f4a22 100%)" role="img" aria-label="Waterfall beneath a railway bridge in autumn forest"></div>
  <div class="abs stem" style="left:247px;top:1505px;height:100px"></div>
  <div class="abs cat label" style="left:148px;top:1605px"><span>Nature</span></div>

  <div class="abs card" style="left:440px;top:1295px;width:320px;height:321px;background:linear-gradient(180deg,#2f5fb8 0%,#6b8fd0 35%,#e07a2c 55%,#8a4a32 75%,#3a2a28 100%)" role="img" aria-label="Sunburst through a desert rock arch"></div>
  <div class="abs stem" style="left:599px;top:1560px;height:92px"></div>
  <div class="abs cat label" style="left:500px;top:1652px"><span>Landscape</span></div>

  <div class="abs card" style="left:791px;top:1345px;width:321px;height:321px;background:linear-gradient(180deg,#8fb7e0 0%,#b0c6dc 35%,#b07a5a 55%,#9a8a74 80%,#7a6a56 100%)" role="img" aria-label="Bighorn sheep in desert scrub"></div>
  <div class="abs stem" style="left:950px;top:1610px;height:90px"></div>
  <div class="abs cat label" style="left:851px;top:1700px"><span>Wildlife</span></div>

  <div class="abs arrow" style="left:212px;top:1789px"><svg width="10" height="10" viewBox="0 0 10 10"><path d="M6.5 1.5 3 5l3.5 3.5" fill="none" stroke="#111" stroke-width="1.5"/></svg></div>
  <div class="abs arrow" style="left:254px;top:1789px"><svg width="10" height="10" viewBox="0 0 10 10"><path d="M3.5 1.5 7 5 3.5 8.5" fill="none" stroke="#111" stroke-width="1.5"/></svg></div>
</section>

<section class="about">
  <h2 class="abs display about-title">About<br>Me</h2>
  <p class="abs copy" style="left:487px;top:2002px;width:515px">Lorem ipsum dolor sit amet, consectetur adipiscing elit. Aenean mattis mi quis tellus convallis, sit amet aliquet massa ornare. Orci varius natoque penatibus et magni. Lorem dolor sit amet, consectetur adipiscing elit.</p>
  <div class="abs btn label" style="left:492px;top:2112px;width:121px;height:36px">Read More</div>
</section>

<section class="subscribe">
  <div class="abs subscribe-bg" role="img" aria-label="Tropical resort terrace with thatched roof and greenery"></div>
  <div class="abs subscribe-box">
    <h2 class="display">Subscribe</h2>
    <p>Sign up with your email address to receive new updates.</p>
    <div class="signup">
      <div class="field">name@mail.com</div>
      <div class="btn label">Sign Up</div>
    </div>
  </div>
</section>

<section class="instagram">
  <div class="abs insta-word" style="left:57px;top:2668px">Insta</div>
  <div class="abs tile" style="left:88px;top:2780px;background:linear-gradient(180deg,#6a9ad6 0%,#dfe6ee 40%,#5a6a70 65%,#2c3a44 100%)" role="img" aria-label="Snowy river gorge under blue sky"></div>
  <div class="abs tile card" style="left:352px;top:2780px;background:linear-gradient(180deg,#c94a2a 0%,#e87a3a 40%,#7a3a4a 65%,#e8e8ee 100%)" role="img" aria-label="Fiery sunset over snowy hills"></div>
  <div class="abs tile" style="left:615px;top:2780px;background:linear-gradient(180deg,#5a2a7a 0%,#c04a8a 45%,#f08a5a 60%,#2a1a3a 100%)" role="img" aria-label="Desert trees silhouetted at purple dusk"></div>
  <div class="abs tile" style="left:879px;top:2780px;background:linear-gradient(180deg,#8a9aa8 0%,#d4d8dc 40%,#3a8a9a 65%,#7a6a5a 100%)" role="img" aria-label="Lake among canyon walls under clouds"></div>
  <div class="abs insta-word" style="left:950px;top:2955px">gram</div>
</section>

<footer>
  <div class="abs footer"></div>
  <div class="abs brand" style="left:88px;top:3282px">Northern Terrain<span class="brand-dot"></span></div>
  <div class="abs legal" style="left:88px;top:3372px">© 2019 Northern Terrain Photography</div>
  <div class="abs foot-link label" style="left:615px;top:3258px">Nature</div>
  <div class="abs foot-link label" style="left:615px;top:3296px">Landscape</div>
  <div class="abs foot-link label" style="left:615px;top:3334px">Wildlife</div>
  <div class="abs foot-link label" style="left:615px;top:3372px">Sunsets</div>
  <div class="abs foot-link label" style="left:615px;top:3412px">Sunrises</div>
  <div class="abs foot-link label" style="left:824px;top:3258px">My Story</div>
  <div class="abs foot-link label" style="left:824px;top:3296px">Gallery</div>
  <div class="abs foot-link label" style="left:824px;top:3334px">Cart</div>
  <div class="abs foot-link label" style="left:824px;top:3372px">Contact</div>
  <div class="abs icon light" style="left:1081px;top:3260px"></div>
  <div class="abs icon light" style="left:1081px;top:3298px"></div>
  <div class="abs icon light" style="left:1081px;top:3336px"></div>
</footer>

</body>
</html>
```